Proyecto Mandril
Stationary
Proyecto Mandril -
Creative Brief
Use specific fonts
Century Gothic
Professional
Ramón Ignacio Bertoldi
Urb. Miraflores Calle Los Pinos Casa 27C Panamá City Panamá
ramon@lacasadelpanvivo.com
We have created business cards in the past and we would like to keep some consistency. We are uploanding those for your reference (front and back of the card). However, we only have business cards, we don't have other stationary and we are looking for a complete set. Thanks for considering our project and we look foraward to receiving your drafts. Best, Talia & Nora
www.lacasadelpanvivo.com

```html
<!DOCTYPE html>
<html lang="es">
<head>
<meta charset="utf-8">
<title>Proyecto Mandril – Tarjetas de presentación</title>
<link rel="stylesheet" href="https://fonts.googleapis.com/css2?family=Questrial&family=Libre+Baskerville&display=swap">
<style>
  :root {
    --page: #ffffff;
    --label: #8a8a8a;
    --brown: #5b4636;
    --brown-text: #dccfc1;
    --brown-rule: #b9a896;
    --paper: #ffffff;
    --paper-edge: #e4e4e4;
    --taupe: #b5a99c;
    --mark: #4a3a2e;
    --mark-light: #f1e9dd;
    --art-dark: #6f6f6f;
    --art-light: #c9c9c9;
    --url: #8c8178;
  }
  * { box-sizing: border-box; margin: 0; padding: 0; }
  html, body {
    width: 1200px; height: 370px; overflow: hidden;
    background: var(--page);
    font-family: "Questrial", "Century Gothic", sans-serif;
  }
  .sheet { position: relative; width: 1200px; height: 370px; }
  .side-label {
    position: absolute; left: 48px; top: 14px;
    font-family: "Libre Baskerville", serif;
    font-size: 22px; letter-spacing: 2px; color: var(--label);
  }
  .card { position: absolute; top: 96px; width: 356px; height: 240px; }
  .card--contact { left: 29px; background: var(--brown); }
  .card--white { left: 427px; background: var(--paper); border: 1px solid var(--paper-edge); }
  .card--taupe { left: 816px; background: var(--taupe); }

  .brand {
    position: absolute; width: 120px;
    display: flex; flex-direction: column; align-items: center;
  }
  .brand__art {
    width: 96px; height: 60px; border-radius: 4px;
    background: linear-gradient(135deg, var(--art-light), var(--art-dark));
  }
  .brand__name {
    margin-top: 6px; text-align: center; white-space: nowrap;
    font-size: 13px; line-height: 15px; color: var(--mark);
  }
  .brand__line { display: block; }
  .card--contact .brand { left: 22px; top: 62px; }
  .card--contact .brand__name { color: var(--mark-light); }
  .card--white .brand, .card--taupe .brand { left: 118px; top: 58px; }

  .divider {
    position: absolute; left: 166px; top: 56px; width: 1px; height: 130px;
    background: var(--brown-rule);
  }
  .contact { position: absolute; left: 184px; top: 60px; right: 12px; color: var(--brown-text); }
  .contact__name { font-size: 12px; line-height: 14px; margin-bottom: 20px; white-space: nowrap; }
  .contact__phone { font-size: 8.5px; line-height: 14px; }
  .contact__email { position: absolute; top: 124px; font-size: 8.5px; white-space: nowrap; }

  .web {
    position: absolute; left: 0; right: 0; top: 178px;
    text-align: center; font-size: 9px; color: var(--url);
  }
  .card--taupe .web { color: var(--mark); }
</style>
</head>
<body>
<main class="sheet">
  <div class="side-label">FRONT</div>

  <section class="card card--contact">
    <div class="brand">
      <div class="brand__art" role="img" aria-label="Ilustración de la marca"></div>
      <div class="brand__name"><span class="brand__line">La Casa</span><span class="brand__line">del Pan Vivo</span></div>
    </div>
    <div class="divider"></div>
    <div class="contact">
      <p class="contact__name">Ramón Ignacio Bertoldi</p>
      <p class="contact__phone">+507 6000 2418</p>
      <p class="contact__phone">+507 6000 7352</p>
      <p class="contact__email">ramon@lacasadelpanvivo.com</p>
    </div>
  </section>

  <section class="card card--white">
    <div class="brand">
      <div class="brand__art" role="img" aria-label="Ilustración de la marca"></div>
      <div class="brand__name"><span class="brand__line">La Casa</span><span class="brand__line">del Pan Vivo</span></div>
    </div>
    <p class="web">www.lacasadelpanvivo.com</p>
  </section>

  <section class="card card--taupe">
    <div class="brand">
      <div class="brand__art" role="img" aria-label="Ilustración de la marca"></div>
      <div class="brand__name"><span class="brand__line">La Casa</span><span class="brand__line">del Pan Vivo</span></div>
    </div>
    <p class="web">www.lacasadelpanvivo.com</p>
  </section>
</main>
</body>
</html>
```